Legal Service Estimated Retainer and Average Case Value

We need an 11x14 flyer that contains the standard retainers and average cost be case, both provided in documents, for each case type we handle. We need the information displayed, preferably in a way that makes the information readable but less troubling to a client shocked at price of litigation. We need one sheet with the retainers and average case value merged into one table.

Target Market(s)

Potential Clients

Font styles to use
Serif
Sans Serif

```html
<!DOCTYPE html>
<html lang="en">
<head>
<meta charset="utf-8">
<title>Legal Service Estimated Retainer &amp; Average Case Value</title>
<link rel="stylesheet" href="https://fonts.googleapis.com/css2?family=Cinzel:wght@400;500&family=Source+Sans+3:wght@400;500&display=swap">
<style>
:root{
  --navy-deep:#12143f;
  --navy:#1c2a78;
  --royal:#1b4597;
  --ink:#1a1f4a;
  --label:#1d3f98;
  --value:#3a3f55;
  --row-a:#f2f3f6;
  --row-b:#e6e9f1;
  --line:#d3d6de;
  --page:#f7f8fb;
  --backdrop:#e4e5e8;
}
*{box-sizing:border-box;margin:0;padding:0}
html,body{width:1087px;height:1200px;overflow:hidden;background:var(--backdrop)}
.flyer{
  position:absolute;left:72px;top:0;width:943px;height:1200px;
  background:linear-gradient(180deg,#fff 0%,var(--page) 60%,#e5e8f0 100%);
  font-family:"Source Sans 3",sans-serif;color:var(--ink);overflow:hidden;
}
.masthead{
  position:absolute;left:0;top:0;width:100%;height:233px;
  background:radial-gradient(ellipse at 45% 50%,#1f3290 0%,var(--navy) 35%,var(--navy-deep) 85%);
}
.masthead-decor{
  position:absolute;left:18px;top:10px;width:200px;height:223px;
  background:linear-gradient(180deg,rgba(255,255,255,.07),rgba(255,255,255,.03));
}
.firm-name{
  position:absolute;left:60px;top:105px;
  font-family:"Cinzel",serif;color:#fff;line-height:1;
}
.firm-name small{display:block;font-size:10px;letter-spacing:.5px;margin-bottom:3px}
.firm-name span{font-size:21px;letter-spacing:.3px}
.title{
  position:absolute;right:52px;top:74px;text-align:right;
  font-family:"Cinzel",serif;font-weight:500;color:#fff;font-size:31px;line-height:37px;letter-spacing:.5px;
}
.stripe{position:absolute;left:0;top:233px;width:100%;height:16px;background:var(--royal)}
.intro{
  position:absolute;left:52px;top:297px;width:838px;
  font-size:20.4px;line-height:28.5px;color:var(--ink);letter-spacing:-.25px;word-spacing:-.5px;
}
.fees{
  position:absolute;left:52px;top:458px;width:838px;border-collapse:collapse;
  box-shadow:0 2px 4px rgba(0,0,0,.18);
}
.fees th{
  height:52px;background:var(--royal);color:#fff;font-family:"Cinzel",serif;font-weight:400;
  font-size:16.5px;letter-spacing:.4px;
}
.fees th.left{text-align:left;padding-left:14px;border-radius:5px 0 0 0;border-right:1px solid #5a78bd}
.fees th.right{border-radius:0 5px 0 0}
.fees td{height:43px;border-bottom:1px solid var(--line);vertical-align:middle}
.fees .lbl{color:var(--label);font-size:13.4px;line-height:14px;padding-left:14px;background:var(--row-a)}
.fees .val{color:var(--value);font-size:11px;text-align:center;background:var(--row-b);line-height:13px}
.fees .sep{border-right:1px solid var(--line)}
.fees .pfa td{vertical-align:top;padding-top:7px}
.col-ll{width:303px}.col-lv{width:119px}.col-rl{width:296px}.col-rv{width:120px}
.footer-band{
  position:absolute;left:0;bottom:0;width:100%;height:29px;
  background:linear-gradient(100deg,#111638 0%,var(--navy) 45%,var(--navy-deep) 50.5%,#fff 50.6%,#fff 51%,var(--royal) 51.1%);
}
</style>
</head>
<body>
<div class="flyer">
  <header class="masthead">
    <div class="masthead-decor" role="img" aria-label="Faint classical column decoration"></div>
    <div class="firm-name"><small>THE LAW OFFICE OF</small><span>MARCUS T ELLERY</span></div>
    <h1 class="title">LEGAL SERVICE<br>ESTIMATED RETAINER &amp;<br>AVERAGE CASE VALUE</h1>
  </header>
  <div class="stripe"></div>
  <p class="intro">In order for our clients to set expectations for legal fees, we provide the national average range of fees per case type. These are only to provide you with an understanding of what other cases have cost clients in similar cases. Please note these are not estimates nor guarantees of your own legal costs.</p>
  <table class="fees">
    <colgroup><col class="col-ll"><col class="col-lv"><col class="col-rl"><col class="col-rv"></colgroup>
    <thead><tr><th class="left" colspan="2">Retainers and Total Estimated Case Costs</th><th class="right" colspan="2">Average Fee Per Case Type</th></tr></thead>
    <tbody>
      <tr><td class="lbl">Divorce (3301 C):<br>Retainer:</td><td class="val sep">$2,000</td><td class="lbl">Custody Contempt/Modification:</td><td class="val">$5,000 - $8,000</td></tr>
      <tr><td class="lbl">Divorce (3301 D):<br>Retainer:</td><td class="val sep">$2,500</td><td class="lbl">Custody Initial Order:</td><td class="val">$4,000 - $7,000</td></tr>
      <tr><td class="lbl">Divorce and Custody:<br>Retainer:</td><td class="val sep">$3,500</td><td class="lbl">Custody &amp; Support:</td><td class="val">$5,000 - $8,000</td></tr>
      <tr><td class="lbl">Divorce and Equitable Distribution:<br>Retainer:</td><td class="val sep">$3,500</td><td class="lbl">Support:</td><td class="val">$2,000 - $4,000</td></tr>
      <tr><td class="lbl">Divorce and Support:<br>Retainer:</td><td class="val sep">$3,000</td><td class="lbl">Divorce (3301c):</td><td class="val">$1,500 - $3,000</td></tr>
      <tr><td class="lbl">Divorce, Custody and Support:<br>Retainer:</td><td class="val sep">$3,500</td><td class="lbl">Divorce (3301d):</td><td class="val">$2,000 - $3,000</td></tr>
      <tr><td class="lbl">Divorce, Equitable Distribution and Support:<br>Retainer:</td><td class="val sep">$3,500</td><td class="lbl">Protection from Abuse:</td><td class="val">$1,500 - $3,000</td></tr>
      <tr><td class="lbl">Divorce, Equitable Distribution and Custody:<br>Retainer:</td><td class="val sep">$5,000</td><td class="lbl">Divorce &amp; Custody:</td><td class="val">$5,000 - $8,000</td></tr>
      <tr><td class="lbl">Divorce, Equitable Distribution, Custody and<br>Support: Retainer:</td><td class="val sep">$3,500</td><td class="lbl">Divorce &amp; Equitable Distribution:</td><td class="val">$6,000 - $10,000</td></tr>
      <tr><td class="lbl">Custody Initial Order:<br>Retainer:</td><td class="val sep">$3,000</td><td class="lbl">Divorce, Custody &amp; Support:</td><td class="val">$8,000 - $12,000</td></tr>
      <tr><td class="lbl">Custody Modification:<br>Retainer:</td><td class="val sep">$3,500</td><td class="lbl">Divorce, Equitable Distribution &amp; Custody:</td><td class="val">$10,000 - $15,000</td></tr>
      <tr><td class="lbl">Custody and Support:<br>Retainer:</td><td class="val sep">$3,000</td><td class="lbl">Divorce, Equitable Distribution &amp; Support:</td><td class="val">$8,000 - $12,000</td></tr>
      <tr class="pfa"><td class="lbl">(PFA) Protection From Abuse:</td><td class="val sep">$2,000<br>Paid In Full</td><td class="lbl">Divorce, Equitable Distribution, Custody<br>&amp; Support:</td><td class="val">$12,000 - $15,000</td></tr>
    </tbody>
  </table>
  <div class="footer-band"></div>
</div>
</body>
</html>
```